Business Card Design

The image I attached was a quick thought to my design. I have triplets and was invisioning something with three figures with maybe the colors blue, pink and green. I would like it to look very chic and modern yet soothing/healing. I will take any fresh ideas as well.

Side 1: Contact Details
Side 2: Appointment section (mandatory)
Updates

Thank u all for your preliminary designs. I had sent the old design over and am looking for a bold fresh NEW LOOK  for CORE MOTION. I saw some really creative ideas in the gallery. If you have any other questions please feel free to email me at rtbwakes@quellmail.net.

Thanks

Please keep in mind that it is mandatory that on the back of the card is for appointments.

Thank you.

Reason: The two mandatory elements that need to be on the card is that her title needs to read as so:

Reason: The criteria is still not being met. Her title needs to read as so: Dr. Marisa Kettner, P.T., D.P.T. Doctor of Physical Therapy and The appointment info must go on the BACK of the card. Looking forward to some more great designs. Thanks.

Industry/Entity Type

Business

Contact Information for Business Card

Core Motion
Physical & Aquatic Therapy
Dr. Marisa Kettner, P.T., D.P.T.
Doctor of Physical Therapy

22-48 B Birchwick Lane
Elmbury, N.Y. 11592
(Located inside of the Summit gym in the Pinecrest shopping center)

Phone & Fax: (631) 555-0172
Mkettner4@harbornet.net

Requirements
Must have
• One the back I would like to do an appointment layout.

```html
<!DOCTYPE html>
<html lang="en">
<head>
<meta charset="utf-8">
<title>Core Motion – Business Card</title>
<link rel="stylesheet" href="https://fonts.googleapis.com/css2?family=Open+Sans:wght@400;600;700&display=swap">
<style>
  :root {
    --navy: #3a3186;
    --orange: #f28a1e;
    --white: #ffffff;
    --ink: #333333;
    --page: #f4f4f4;
  }
  * { box-sizing: border-box; margin: 0; padding: 0; }
  html, body { width: 1073px; height: 1200px; overflow: hidden; }
  body {
    background: var(--page);
    font-family: "Open Sans", Arial, sans-serif;
    position: relative;
  }
  .card {
    position: absolute;
    width: 844px;
    height: 468px;
    background: var(--white);
    border-radius: 28px;
    overflow: hidden;
    box-shadow: 0 6px 14px rgba(0,0,0,0.18);
  }
  .card--front { left: 112px; top: 98px; }
  .card--back  { left: 118px; top: 629px; }
  .card__waves { position: absolute; inset: 0; width: 100%; height: 100%; }

  .brand {
    position: absolute;
    left: 40px;
    top: 215px;
    width: 260px;
    text-align: center;
    color: var(--navy);
  }
  .brand__name {
    font-weight: 700;
    font-size: 28px;
    display: inline-flex;
    align-items: center;
    gap: 10px;
  }
  .brand__dot {
    width: 16px; height: 16px; border-radius: 50%;
    background: var(--orange);
  }
  .brand__tagline { font-size: 18px; margin-top: 2px; }

  .contact {
    position: absolute;
    right: 71px;
    text-align: right;
    color: var(--ink);
  }
  .contact__name { top: 44px; font-size: 26px; font-weight: 700; color: var(--navy); }
  .contact__title { top: 102px; font-size: 23px; }
  .contact__line {
    display: flex; align-items: center; justify-content: flex-end; gap: 8px;
  }
  .contact__phone { top: 147px; font-size: 25px; letter-spacing: 0.5px; }
  .contact__email { top: 198px; font-size: 24px; }
  .contact__address { top: 316px; font-size: 24px; color: var(--white); line-height: 37px; }
  .contact__located { top: 395px; font-size: 21px; color: var(--white); }
  .icon { width: 24px; height: 24px; flex: none; }

  .appointment__heading {
    position: absolute; left: 104px; top: 66px;
    color: var(--white); font-weight: 700; font-size: 25px;
  }
  .appointment__brand {
    position: absolute; right: 36px; top: 122px;
    color: var(--navy); font-weight: 700; font-size: 26px;
    display: inline-flex; align-items: center; gap: 9px;
  }
  .appointment__field {
    position: absolute; left: 166px;
    display: flex; align-items: flex-end;
    color: var(--navy); font-size: 22px;
  }
  .appointment__field--date { top: 252px; }
  .appointment__field--time { top: 352px; }
  .appointment__rule {
    display: inline-block; width: 430px; margin-left: 6px;
    border-bottom: 1.5px solid var(--navy); margin-bottom: 4px;
  }
</style>
</head>
<body>

<section class="card card--front">
  <svg class="card__waves" viewBox="0 0 715 397" preserveAspectRatio="none" aria-hidden="true">
    <path fill="var(--orange)" d="M0,300 C120,330 260,318 380,278 C480,242 600,206 715,204 L715,226 C620,224 520,242 430,268 C300,306 130,336 0,318Z"/>
    <path fill="var(--navy)" d="M0,328 C140,342 300,318 430,275 C540,240 630,226 715,230 L715,397 L0,397Z"/>
  </svg>

  <div class="brand">
    <div class="brand__name"><span class="brand__dot"></span>Core Motion</div>
    <div class="brand__tagline">Physical &amp; Aquatic Therapy</div>
  </div>

  <div class="contact contact__name">Dr. Marisa Kettner, P.T., D.P.T.</div>
  <div class="contact contact__title">Doctor of Physical Therapy</div>
  <div class="contact contact__phone contact__line">
    <svg class="icon" viewBox="0 0 24 24" aria-hidden="true"><path fill="var(--ink)" d="M6.6 2.5l3 3.6-1.8 2.3c1.2 2.8 3.3 5 6 6.3l2.3-1.7 3.5 3-2 3.2C11 18.6 5 12 3.8 4.6z"/></svg>
    <svg class="icon" viewBox="0 0 24 24" aria-hidden="true"><g fill="none" stroke="var(--ink)" stroke-width="1.6"><rect x="6" y="3" width="12" height="7"/><rect x="2.5" y="10" width="19" height="10" rx="1"/><line x1="6" y1="14" x2="18" y2="14"/><line x1="6" y1="17" x2="18" y2="17"/></g></svg>
    <span>(631) 555-0172</span>
  </div>
  <div class="contact contact__email contact__line">
    <svg class="icon" viewBox="0 0 24 24" aria-hidden="true"><g fill="none" stroke="var(--ink)" stroke-width="1.6"><rect x="2" y="5" width="20" height="14"/><path d="M2 5l10 8 10-8"/></g></svg>
    <span>Mkettner4@harbornet.net</span>
  </div>
  <div class="contact contact__address">
    <div class="contact__line">
      <svg class="icon" viewBox="0 0 24 24" aria-hidden="true"><path fill="var(--white)" d="M12 3L2 10h2v11h16V10h2zM7 13h4v6H7zm6 0h4v6h-4z"/></svg>
      <span>22-48 B Birchwick Lane</span>
    </div>
    <div>Elmbury, N.Y. 11592</div>
  </div>
  <div class="contact contact__located">Located inside of the Summit gym in the Pinecrest shopping center</div>
</section>

<section class="card card--back">
  <svg class="card__waves" viewBox="0 0 712 397" preserveAspectRatio="none" aria-hidden="true">
    <path fill="var(--navy)" d="M0,0 H712 V20 C600,24 500,55 400,95 C260,145 120,160 0,156Z"/>
    <path fill="var(--white)" d="M0,108 C150,126 300,106 420,70 C540,36 640,22 712,24 V30 C630,30 540,44 430,78 C300,118 150,138 0,114Z"/>
    <path fill="var(--orange)" d="M0,114 C150,132 300,112 420,76 C540,42 640,28 712,30 V46 C630,44 540,62 440,92 C300,134 150,148 0,134Z"/>
  </svg>

  <div class="appointment__heading">Next appointment:</div>
  <div class="appointment__brand"><span class="brand__dot"></span>Core Motion</div>

  <div class="appointment__field appointment__field--date">Date<span class="appointment__rule"></span></div>
  <div class="appointment__field appointment__field--time">Time<span class="appointment__rule"></span></div>
</section>

</body>
</html>
```